business card and flyer/pricelist

Business Name: Fern Locks Westbrook
new boutique salon run from home, using Australian owned natural products and colours, we need a flyer design to do a letter box drop to advertise the business as well as incorporating a price list on the front (single sided with writing on front and only colour on back)

The salon has a natural feel with light coloured timber chairs, bamboo timber bench top and shelving.

we are after a natural toned colour for the flyer, with possibly a brown/darkish colour writing

we are after a flyer that will also be able to use the design heading (business name) for business cards as well

feel free to look on my pintrest account to get a feel for my style under Marla Quenby.

I love simple clean and Natural looks.

Font styles to use
Script
Other font styles liked:
• SCRIPT HANDWRITTEN FONTS

Colors
cadf82
e9f1ce
5c5c5c
d3d3d3
add136
fee18a

Requirements
Must have
• NATURAL COLOURINGS, eg soft greens, browns,
white or off white background.
Should not have
• photos,

```html
<!DOCTYPE html>
<html lang="en">
<head>
<meta charset="UTF-8">
<title>Fern Locks Westbrook – Price List</title>
<link href="https://fonts.googleapis.com/css2?family=Ubuntu:wght@400;500&display=swap" rel="stylesheet">
<style>
  :root {
    --ink: #4a3524;
    --lime: #aaff00;
    --lime-soft: #c8ff66;
    --band: #c2ff4d;
    --bg-top: #d9ffc4;
    --bg-mid: #fffff2;
    --bg-bottom: #f6fbc6;
    --foliage: rgba(196, 240, 150, 0.45);
    --divider: rgba(74, 53, 36, 0.35);
  }
  * { margin: 0; padding: 0; box-sizing: border-box; }
  html, body { width: 1200px; height: 2609px; overflow: hidden; }
  body {
    position: relative;
    font-family: "Ubuntu", sans-serif;
    color: var(--ink);
    background: linear-gradient(180deg, var(--bg-top) 0%, var(--bg-mid) 45%, var(--bg-mid) 65%, var(--bg-bottom) 84%);
  }
  .foliage {
    position: absolute;
    top: 0;
    width: 380px;
    height: 1300px;
  }
  .foliage--left {
    left: 0;
    background: radial-gradient(ellipse 70% 55% at 10% 45%, var(--foliage), transparent 70%);
  }
  .foliage--right {
    right: 0;
    background: radial-gradient(ellipse 70% 45% at 90% 30%, var(--foliage), transparent 70%);
  }
  .masthead {
    position: absolute;
    left: 234px;
    top: 0;
    width: 728px;
    height: 615px;
    background: var(--lime);
    text-align: center;
  }
  .masthead::before {
    content: "";
    position: absolute;
    left: 0; top: 0; right: 0;
    height: 68px;
    background: var(--lime-soft);
  }
  .masthead__name {
    position: absolute;
    left: 0; right: 0;
    top: 322px;
    font-size: 138px;
    font-weight: 400;
    line-height: 1;
    letter-spacing: -2px;
  }
  .masthead__place {
    position: absolute;
    left: 0; right: 0;
    top: 478px;
    font-size: 41px;
    font-weight: 400;
    letter-spacing: 21px;
    padding-left: 21px;
  }
  .flourish {
    position: absolute;
    left: 517px;
    width: 166px;
    height: 89px;
    background: radial-gradient(ellipse at center, rgba(74, 53, 36, 0.55), rgba(74, 53, 36, 0.15) 60%, transparent 72%);
  }
  .flourish--top { top: 709px; }
  .flourish--bottom { top: 1990px; }
  .price-list {
    position: absolute;
    left: 95px;
    top: 899px;
    width: 1010px;
    list-style: none;
  }
  .price-list__item {
    display: flex;
    justify-content: space-between;
    height: 103.6px;
    font-size: 41px;
    line-height: 50px;
  }
  .price-list__price { width: 150px; }
  .contact-band {
    position: absolute;
    left: 0; right: 0;
    top: 2182px;
    bottom: 0;
    background: var(--band);
  }
  .contact {
    position: absolute;
    top: 2271px;
    font-size: 41px;
    line-height: 52px;
  }
  .contact--person { left: 122px; }
  .contact--address { left: 533px; top: 2265px; }
  .contact-divider {
    position: absolute;
    left: 485px;
    top: 2218px;
    width: 2px;
    height: 222px;
    background: var(--divider);
  }
  .website {
    position: absolute;
    left: 0; right: 0;
    top: 2475px;
    text-align: center;
    font-size: 46px;
  }
</style>
</head>
<body>
  <div class="foliage foliage--left" role="img" aria-label="Faint leafy tree silhouettes"></div>
  <div class="foliage foliage--right" role="img" aria-label="Faint leafy tree silhouettes"></div>

  <header class="masthead">
    <h1 class="masthead__name">Fern Locks</h1>
    <p class="masthead__place">WESTBROOK</p>
  </header>

  <div class="flourish flourish--top" role="img" aria-label="Decorative flourish ornament"></div>

  <ul class="price-list">
    <li class="price-list__item"><span>Oil Treatment</span><span class="price-list__price">$23.05</span></li>
    <li class="price-list__item"><span>Naturals 16 oz. Volumizing Shampoo</span><span class="price-list__price">$21.82</span></li>
    <li class="price-list__item"><span>Vanilla Moisturizing Hair Duo</span><span class="price-list__price">$40.00</span></li>
    <li class="price-list__item"><span>Hair Milk Nourishing Refresher Spray</span><span class="price-list__price">$22.82</span></li>
    <li class="price-list__item"><span>Repairing Hair Mask</span><span class="price-list__price">$36.36</span></li>
    <li class="price-list__item"><span>Color Care Moisturizing Hair Oil</span><span class="price-list__price">$21.82</span></li>
    <li class="price-list__item"><span>Heat &amp; Humidity Gel</span><span class="price-list__price">$56.05</span></li>
    <li class="price-list__item"><span>Naturals Volumizing Shampoo</span><span class="price-list__price">$9.99</span></li>
    <li class="price-list__item"><span>Tonic Lotion</span><span class="price-list__price">$9.50</span></li>
    <li class="price-list__item"><span>Hair Building Fibers</span><span class="price-list__price">$22.82</span></li>
  </ul>

  <div class="flourish flourish--bottom" role="img" aria-label="Decorative flourish ornament"></div>

  <footer>
    <div class="contact-band"></div>
    <p class="contact contact--person">Marla Quenby<br>+ 61 7345550182</p>
    <div class="contact-divider"></div>
    <p class="contact contact--address">Westbrook, QLD, 4350<br>info@fernlockswestbrook.com</p>
    <p class="website">www.fernlockswestbrook.net</p>
  </footer>
</body>
</html>
```